Business Card Designs

Looking to design a 3.5" x 2" standard business card for our employees.
The design needs to be sleek, simple, and modern. We would like our logo (attached) to be incorporated, but not in that colour, rather an outline of the logo in either gold or silver (whichever looks better).

Modern and Simple is what we are looking for, but be creative in incorporating the logo.

```html
<!DOCTYPE html>
<html lang="en">
<head>
<meta charset="UTF-8">
<title>Harbourline Boutique Suites – Business Card</title>
<link href="https://fonts.googleapis.com/css2?family=Roboto+Condensed:wght@400;500&family=Montserrat:wght@400;600&display=swap" rel="stylesheet">
<style>
  :root {
    --backdrop: #7a6850;
    --card: #232323;
    --card-shadow: rgba(0,0,0,0.55);
    --teal: #5fa3a0;
    --teal-soft: #6f9493;
    --ink-light: #f1f1f1;
    --mark-fill: #2d2d2d;
    --emboss: #4a4a4a;
  }
  * { margin: 0; padding: 0; box-sizing: border-box; }
  html, body { width: 900px; height: 1200px; overflow: hidden; }
  body {
    background: var(--backdrop);
    position: relative;
    font-family: "Montserrat", sans-serif;
  }
  .card {
    position: absolute;
    left: 80px;
    width: 742px;
    height: 440px;
    background: var(--card);
    border-radius: 30px;
    box-shadow: 0 6px 14px var(--card-shadow);
  }
  .card--front { top: 132px; }
  .card--back { top: 640px; height: 438px; }

  .brand-name {
    position: absolute;
    left: 33px;
    top: 62px;
    font-family: "Roboto Condensed", sans-serif;
    font-weight: 500;
    color: var(--teal);
    text-transform: uppercase;
    text-align: center;
    line-height: 1.2;
  }
  .brand-name__line1 { display: block; font-size: 28px; letter-spacing: 2.5px; }
  .brand-name__line2 { display: block; font-size: 25px; letter-spacing: 4px; }

  .brand-square {
    position: absolute;
    left: 405px;
    top: 48px;
    width: 295px;
    height: 365px;
    background: var(--mark-fill);
  }

  .person { position: absolute; left: 31px; top: 198px; }
  .person__name { font-size: 26px; font-weight: 600; color: var(--teal); line-height: 1.1; }
  .person__role { font-size: 15px; color: var(--ink-light); margin-top: 2px; }

  .address {
    position: absolute;
    left: 36px;
    top: 267px;
    font-size: 16px;
    line-height: 20px;
    color: var(--ink-light);
    font-style: normal;
  }

  .contacts { position: absolute; left: 36px; top: 332px; list-style: none; }
  .contacts li {
    display: flex;
    align-items: center;
    gap: 8px;
    height: 24.5px;
    font-size: 16px;
    color: var(--ink-light);
  }
  .contacts svg { width: 16px; height: 16px; fill: var(--teal); }

  .back-square {
    position: absolute;
    left: 296px;
    top: 80px;
    width: 150px;
    height: 190px;
    background: var(--mark-fill);
  }
  .back-name {
    position: absolute;
    left: 0;
    right: 0;
    top: 328px;
    text-align: center;
    font-family: "Roboto Condensed", sans-serif;
    font-weight: 500;
    color: var(--emboss);
    text-transform: uppercase;
    line-height: 1.25;
  }
  .back-name span { display: block; }
  .back-name__line1 { font-size: 28px; letter-spacing: 3px; }
  .back-name__line2 { font-size: 24px; letter-spacing: 5px; }
</style>
</head>
<body>
  <section class="card card--front">
    <h1 class="brand-name">
      <span class="brand-name__line1">Harbourline Boutique</span>
      <span class="brand-name__line2">Suites</span>
    </h1>
    <div class="brand-square"></div>

    <div class="person">
      <p class="person__name">Daniel Reyes</p>
      <p class="person__role">owner</p>
    </div>

    <address class="address">4820 Lakeview Avenue, Suite 305<br>Riverton, FL 33410</address>

    <ul class="contacts">
      <li>
        <svg viewBox="0 0 16 16" aria-hidden="true"><path d="M2 6c0-2 3-3 6-3s6 1 6 3v1h-3V6H5v1H2zM4 8h8l1 5H3z"/></svg>
        (555) 014-2287
      </li>
      <li>
        <svg viewBox="0 0 16 16" aria-hidden="true"><path d="M2 4h12v1L8 9 2 5zM2 6.5l6 4 6-4V12H2z"/></svg>
        hello@harbourline.com
      </li>
      <li>
        <svg viewBox="0 0 16 16" aria-hidden="true"><circle cx="8" cy="8" r="6.5"/></svg>
        www.harbourlinesuites.com
      </li>
    </ul>
  </section>

  <section class="card card--back">
    <div class="back-square"></div>
    <p class="back-name">
      <span class="back-name__line1">Harbourline Boutique</span>
      <span class="back-name__line2">Suites</span>
    </p>
  </section>
</body>
</html>
```